Finch Haulage Ltd

We need an A5 size (UK size) flyer to advertise our new business which is called Finch Haulage.
Domestic and Commercial Waste Clearance Services.
Please have the question in bold "Do you have a pile of junk you need to dispose of?"
We collect all kinds of junk or rubbish from homes and businesses across Kent, Sussex and South London.
No fuss, no mess!
A low cost, hassle free alternative to skip hire.
Licensed by the Landcare Board and fully insured (this can be in small print at the bottom).
Please put the Recycle symbol somewhere.
Our tagline on our vehicle is "We Clear More, For Less!"
We'd like the flyer to be bold and eye-catching (to catch the eye of the homeowner or business owner while it's sitting on their doormat).
We need our telephone, website and email to be prominent. Maybe saying "Call today for a free quote"
Tel. 01734 586019
Email: info@finchhaulage.example.co.uk
www.finchhaulage.example.co.uk
Target Market(s)
Our market will be homes and small businesses around Kent, Sussex and South London.

```html
<!DOCTYPE html>
<html lang="en">
<head>
<meta charset="utf-8">
<title>Finch Haulage – Waste Clearance Flyer</title>
<link href="https://fonts.googleapis.com/css2?family=Roboto:wght@300;400;700;900&display=swap" rel="stylesheet">
<style>
  :root {
    --accent: #ffee1f;
    --ink: #ffffff;
    --ground-dark: #111111;
    --ground-mid: #2e2e2e;
    --muted: #8a8a8a;
    --rule: #9a9a9a;
  }
  * { margin: 0; padding: 0; box-sizing: border-box; }
  html, body {
    width: 846px; height: 1200px; overflow: hidden;
    background: var(--accent);
  }
  .flyer {
    position: relative;
    width: 846px; height: 1200px;
    background: var(--accent);
    font-family: 'Roboto', sans-serif;
    color: var(--ink);
  }
  .flyer__backdrop {
    position: absolute;
    left: 20px; top: 20px; right: 20px; bottom: 20px;
    background:
      radial-gradient(ellipse at 25% 20%, #3a3a3a 0%, transparent 45%),
      radial-gradient(ellipse at 75% 55%, #353535 0%, transparent 40%),
      radial-gradient(ellipse at 40% 85%, #303030 0%, transparent 45%),
      linear-gradient(160deg, var(--ground-mid), var(--ground-dark));
  }
  .headline {
    position: absolute;
    left: 85px; top: 52px;
    font-weight: 900;
    font-size: 89px;
    line-height: 96px;
    letter-spacing: 0.5px;
    text-transform: uppercase;
  }
  .headline .highlight { color: var(--accent); }
  .intro {
    position: absolute;
    left: 81px; top: 678px;
    display: flex; align-items: center; gap: 34px;
  }
  .intro__icon { width: 88px; height: 88px; flex: none; }
  .intro__text {
    font-weight: 300;
    font-size: 27.5px;
    line-height: 35px;
    width: 560px;
  }
  .divider {
    position: absolute;
    left: 85px; top: 829px;
    width: 676px; height: 1.5px;
    background: var(--rule);
  }
  .contacts {
    position: absolute;
    left: 85px; top: 898px;
    list-style: none;
  }
  .contacts__item {
    display: flex; align-items: center;
    height: 59px;
    font-weight: 400;
    font-size: 30px;
  }
  .contacts__icon { width: 32px; height: 32px; margin-right: 22px; flex: none; }
  .licence {
    position: absolute;
    left: 0; right: 0; top: 1110px;
    text-align: center;
    font-weight: 300;
    font-size: 21px;
    color: var(--muted);
  }
</style>
</head>
<body>
<main class="flyer">
  <div class="flyer__backdrop" role="img" aria-label="Close-up photograph of a heap of black rubbish bags"></div>

  <h1 class="headline">
    Do you have<br>
    a <span class="highlight">pile of</span><br>
    <span class="highlight">junk</span> you<br>
    need to<br>
    <span class="highlight">dispose of</span>?
  </h1>

  <section class="intro">
    <svg class="intro__icon" viewBox="-50 -50 100 100" aria-hidden="true">
      <g fill="#ffffff">
        <g id="recycle-arrow">
          <path d="M-6 -38 L6 -38 L22 -10 L30 -15 L26 10 L3 2 L11 -3 L0 -22 L-10 -5 L-20 -11 Z"/>
        </g>
        <use href="#recycle-arrow" transform="rotate(120)"/>
        <use href="#recycle-arrow" transform="rotate(240)"/>
      </g>
    </svg>
    <p class="intro__text">We collect all kinds of junk or rubbish from homes and business. No fuss, no mess! Very competitive prices.</p>
  </section>

  <div class="divider"></div>

  <ul class="contacts">
    <li class="contacts__item">
      <svg class="contacts__icon" viewBox="0 0 32 32" aria-hidden="true">
        <circle cx="16" cy="16" r="13.5" fill="none" stroke="var(--accent)" stroke-width="3"/>
        <path d="M12 9 L15 9 L15 13 L13 14 Q14 18 17 20 L18 18 L22 18 L22 21 Q20 24 17 23 Q10 20 10 12 Q10 10 12 9 Z" fill="var(--accent)"/>
      </svg>
      01734 586019
    </li>
    <li class="contacts__item">
      <svg class="contacts__icon" viewBox="0 0 32 32" aria-hidden="true">
        <rect x="3" y="7" width="26" height="18" fill="none" stroke="var(--accent)" stroke-width="2.5"/>
        <path d="M3 7 L16 18 L29 7 M3 25 L12 15 M29 25 L20 15" fill="none" stroke="var(--accent)" stroke-width="2.5"/>
      </svg>
      info@finchhaulage.example.co.uk
    </li>
    <li class="contacts__item">
      <svg class="contacts__icon" viewBox="0 0 32 32" aria-hidden="true">
        <rect x="3" y="5" width="26" height="22" fill="none" stroke="var(--accent)" stroke-width="2.5"/>
        <line x1="3" y1="11" x2="29" y2="11" stroke="var(--accent)" stroke-width="2.5"/>
      </svg>
      www.finchhaulage.example.co.uk
    </li>
  </ul>

  <p class="licence">Licensed by the Landcare Board and fully insured</p>
</main>
</body>
</html>
```